Poster for Ballet Recital Tomasito y el Espejo Encantado

We need a poster for a ballet performance, we will be presenting "Tomasito y el Espejo Encantado".
We need something that looks magical, the word Tomasito as the main title in 3D gold texture and the text y el Espejo Encantado way smaller. We have included a reference of the Brelvo movie, just because we like the starry night background and the glowing moon. We don't want the two characters nor the flying carpet, because we will be adding a photo later.
The idea is for the poster to look magical, mysterious but fun. We want people to get the idea that the show will be very entertaining and worth their money.

Font styles to use
Decorative
Script

Colors

Designer to choose colors to be used in the design.

Requirements
Must have
• The title: Tomasito y el Espejo Encantado
• It must also include space for adding the ballet company logo, the dates, times and prices.
Nice to have
• Magical feel
Should not have
• Any photo or character illustration

```html
<!DOCTYPE html>
<html lang="es">
<head>
<meta charset="utf-8">
<title>Tomasito y el Espejo Encantado — Ballet Poster</title>
<link rel="stylesheet" href="https://fonts.googleapis.com/css2?family=Playball&family=Cinzel:wght@400;500;600&family=PT+Sans&display=swap">
<style>
  :root {
    --wall: #bdbdbd;
    --night-deep: #030822;
    --night-mid: #0a237a;
    --night-glow: #1c4fd0;
    --ground: #020306;
    --gold-light: #ffe98a;
    --gold-mid: #f0a914;
    --gold-dark: #8f5004;
    --amber: #f0a623;
    --ember: #ff5a12;
    --moon: #dff2ff;
    --moon-edge: #6fb6ff;
    --star: #ffffff;
    --white: #ffffff;
  }
  html, body {
    margin: 0;
    width: 1150px;
    height: 1200px;
    overflow: hidden;
    background: var(--wall);
  }
  .poster {
    position: absolute;
    left: 155px;
    top: 15px;
    width: 840px;
    height: 1170px;
    overflow: hidden;
    background:
      radial-gradient(ellipse 55% 32% at 48% 60%, rgba(70,140,255,.5), transparent 70%),
      linear-gradient(180deg, var(--night-deep) 0%, #061561 22%, var(--night-mid) 45%, var(--night-glow) 68%, #0b1d55 80%, var(--ground) 88%, var(--ground) 100%);
    font-family: "Cinzel", serif;
    color: var(--white);
  }
  .starfield {
    position: absolute;
    inset: 0;
    width: 840px;
    height: 1170px;
  }
  .starfield .star { fill: var(--star); }
  .starfield .sparkle { fill: var(--star); }
  .starfield .dust { fill: #6aa8ff; }
  .logo-slot {
    position: absolute;
    left: 334px;
    top: 46px;
    width: 172px;
    height: 60px;
    border: 1.5px solid var(--white);
    display: flex;
    align-items: center;
    justify-content: center;
    font-family: "PT Sans", sans-serif;
    font-size: 31px;
    box-sizing: border-box;
  }
  .moon {
    position: absolute;
    left: 600px;
    top: 10px;
    width: 220px;
    height: 210px;
  }
  .moon .halo { fill: url(#moonGlow); }
  .moon .crescent {
    fill: var(--moon);
    filter: drop-shadow(0 0 10px var(--moon-edge)) drop-shadow(0 0 22px var(--moon-edge));
  }
  .title {
    position: absolute;
    left: 0;
    right: 0;
    top: 92px;
    margin: 0;
    text-align: center;
    font-family: "Playball", cursive;
    font-weight: 400;
    font-size: 210px;
    line-height: 1;
    letter-spacing: -3px;
    background: linear-gradient(180deg, var(--gold-light) 0%, var(--gold-mid) 40%, var(--gold-dark) 72%, var(--gold-mid) 100%);
    -webkit-background-clip: text;
    background-clip: text;
    color: transparent;
    filter: drop-shadow(2px 4px 2px rgba(0,0,0,.7));
  }
  .subtitle {
    position: absolute;
    right: 75px;
    top: 322px;
    margin: 0;
    font-family: "Playball", cursive;
    font-weight: 400;
    font-size: 46px;
    line-height: 1;
    text-shadow: 0 2px 4px rgba(0,0,0,.6);
  }
  .photo-area {
    position: absolute;
    left: 110px;
    top: 390px;
    width: 620px;
    height: 500px;
    border-radius: 50%;
    background: radial-gradient(ellipse at 50% 50%, rgba(220,235,255,.75) 0%, rgba(120,170,255,.45) 35%, rgba(40,90,220,0) 70%);
  }
  .details {
    position: absolute;
    left: 0;
    right: 0;
    top: 922px;
    text-align: center;
  }
  .date-line {
    margin: 0 0 14px;
    font-size: 24px;
    font-weight: 500;
    color: var(--amber);
  }
  .headline {
    margin: 0;
    font-size: 40px;
    font-weight: 400;
    line-height: 1;
  }
  .headline span {
    display: block;
    padding-bottom: 10px;
    margin-bottom: 6px;
    background: radial-gradient(ellipse 45% 2px at 50% 100%, var(--ember), transparent) no-repeat bottom / 100% 4px;
  }
  .tickets {
    margin: 22px 0 0;
    font-size: 17px;
    color: var(--amber);
  }
</style>
</head>
<body>
  <main class="poster">
    <svg class="starfield" viewBox="0 0 840 1170" aria-hidden="true">
      <g class="star">
        <circle cx="48" cy="32" r="2.2"/><circle cx="120" cy="70" r="1.2"/><circle cx="205" cy="24" r="1.4"/>
        <circle cx="268" cy="88" r="1"/><circle cx="560" cy="40" r="1.3"/><circle cx="600" cy="110" r="1"/>
        <circle cx="790" cy="230" r="1.5"/><circle cx="30" cy="150" r="1"/><circle cx="80" cy="230" r="1.3"/>
        <circle cx="22" cy="320" r="1.1"/><circle cx="150" cy="390" r="1.4"/><circle cx="60" cy="440" r="1"/>
        <circle cx="800" cy="330" r="1.2"/><circle cx="760" cy="420" r="1.5"/><circle cx="690" cy="470" r="1"/>
        <circle cx="810" cy="520" r="1.3"/><circle cx="40" cy="560" r="1.2"/><circle cx="110" cy="620" r="1"/>
        <circle cx="780" cy="600" r="1.1"/><circle cx="720" cy="680" r="1.4"/><circle cx="30" cy="700" r="1.3"/>
        <circle cx="90" cy="760" r="1"/><circle cx="800" cy="760" r="1.2"/><circle cx="470" cy="56" r="1"/>
        <circle cx="330" cy="20" r="1.2"/><circle cx="420" cy="130" r="0.9"/><circle cx="250" cy="420" r="1"/>
        <circle cx="620" cy="400" r="1.1"/><circle cx="180" cy="520" r="0.9"/><circle cx="660" cy="560" r="1"/>
        <circle cx="395" cy="35" r="0.8"/><circle cx="170" cy="150" r="0.9"/><circle cx="740" cy="300" r="0.8"/>
        <circle cx="20" cy="50" r="0.8"/><circle cx="520" cy="390" r="0.9"/><circle cx="300" cy="470" r="0.8"/>
        <circle cx="130" cy="820" r="1"/><circle cx="700" cy="790" r="1"/><circle cx="830" cy="120" r="1"/>
      </g>
      <g class="sparkle">
        <path d="M48 20 L50 30 L60 32 L50 34 L48 44 L46 34 L36 32 L46 30 Z"/>
        <path d="M700 90 L701.5 97 L708 98.5 L701.5 100 L700 107 L698.5 100 L692 98.5 L698.5 97 Z"/>
        <path d="M620 45 L621.5 52 L628 53.5 L621.5 55 L620 62 L618.5 55 L612 53.5 L618.5 52 Z"/>
        <path d="M60 660 L62 670 L72 672 L62 674 L60 684 L58 674 L48 672 L58 670 Z"/>
        <path d="M530 715 L532 724 L541 726 L532 728 L530 737 L528 728 L519 726 L528 724 Z"/>
        <path d="M795 470 L796.5 477 L803 478.5 L796.5 480 L795 487 L793.5 480 L787 478.5 L793.5 477 Z"/>
        <path d="M165 560 L166.5 567 L173 568.5 L166.5 570 L165 577 L163.5 570 L157 568.5 L163.5 567 Z"/>
      </g>
      <g class="dust" opacity=".7">
        <circle cx="700" cy="740" r="1.4"/><circle cx="720" cy="760" r="1.1"/><circle cx="745" cy="745" r="1.3"/>
        <circle cx="690" cy="790" r="1.2"/><circle cx="730" cy="800" r="1"/><circle cx="760" cy="780" r="1.4"/>
        <circle cx="670" cy="830" r="1.1"/><circle cx="705" cy="845" r="1.3"/><circle cx="780" cy="810" r="1"/>
        <circle cx="650" cy="870" r="1.2"/><circle cx="690" cy="880" r="1"/><circle cx="800" cy="760" r="1.2"/>
      </g>
    </svg>

    <div class="logo-slot">Logo Here</div>

    <svg class="moon" viewBox="0 0 220 210" aria-hidden="true">
      <defs>
        <radialGradient id="moonGlow" cx="50%" cy="55%" r="50%">
          <stop offset="0%" stop-color="#8cc8ff" stop-opacity=".55"/>
          <stop offset="100%" stop-color="#8cc8ff" stop-opacity="0"/>
        </radialGradient>
      </defs>
      <circle class="halo" cx="110" cy="110" r="100"/>
      <path class="crescent" d="M160 30 A78 78 0 1 1 38 150 A64 64 0 0 0 160 30 Z"/>
    </svg>

    <h1 class="title">Tomasito</h1>
    <p class="subtitle">y el Espejo Encantado</p>

    <div class="photo-area" role="img" aria-label="Ballerina leaping amid a burst of white powder above glowing night clouds"></div>

    <section class="details">
      <p class="date-line">SATURDAY XX MAY 2019 &nbsp;|&nbsp; 8PM TO 2AM</p>
      <h2 class="headline">
        <span>JOIN US FOR AN EXCLUSIVE</span>
        <span>AND FUN BALLET PERFORMANCE</span>
      </h2>
      <p class="tickets">TICKETS: WWW.WEBSITEADDRESS.COM | PRICE: XXXX</p>
    </section>
  </main>
</body>
</html>
```